Wealth Education Business Needs Sharp Business Card Design

We need a business card design for a recently launched investor education business called Harbor Ledger.

The final design should promote security, empowerment, self improvement and financial gain. The card will ideally promote the stature of the business.

For more information and colours please visit harborledger-example.com.au

Target Market(s)

Corporate executives and high net worth individuals

Industry/Entity Type

Education

Contact Information for Business Card

Name
Position
Contact Address
Phone
Mobile
Email
Website

```html
<!DOCTYPE html>
<html lang="en">
<head>
<meta charset="utf-8">
<title>Harbor Ledger – Business Card</title>
<link rel="stylesheet" href="https://fonts.googleapis.com/css2?family=Open+Sans:wght@400;600;700&display=swap">
<style>
  :root {
    --stage: #0b5a80;
    --card-dark: #434141;
    --card-light: #ffffff;
    --ink: #3f3f3f;
    --brand-teal: #1a9aa0;
    --shadow: rgba(0, 0, 0, 0.35);
  }
  * { box-sizing: border-box; margin: 0; padding: 0; }
  html, body {
    width: 1200px;
    height: 1000px;
    overflow: hidden;
    background: var(--stage);
    font-family: "Open Sans", Arial, sans-serif;
  }
  .card {
    position: absolute;
    left: 302px;
    width: 595px;
    height: 333px;
    overflow: hidden;
    box-shadow: 2px 3px 4px var(--shadow);
  }
  .card-front { top: 145px; background: var(--card-dark); }
  .card-back { top: 521px; height: 331px; background: var(--card-light); }
  .card-shapes { position: absolute; inset: 0; width: 100%; height: 100%; }

  .brand-name {
    position: absolute;
    font-weight: 600;
    letter-spacing: 0.14em;
    text-transform: uppercase;
    white-space: nowrap;
  }
  .card-front .brand-name {
    left: 0; right: 0;
    top: 146px;
    text-align: center;
    font-size: 40px;
    color: var(--card-light);
  }
  .card-back .brand-name {
    right: 28px;
    top: 44px;
    font-size: 27px;
    color: var(--brand-teal);
  }

  .holder {
    position: absolute;
    left: 30px;
    top: 38px;
    color: var(--ink);
    font-size: 18px;
    line-height: 25px;
  }
  .holder .role { font-weight: 700; }

  .contact-list {
    position: absolute;
    left: 30px;
    top: 161px;
    list-style: none;
    color: var(--ink);
    font-size: 15.5px;
    line-height: 22px;
  }
  .contact-list li { margin-bottom: 5px; }
  .contact-list li.address { line-height: 22px; }

  .web-list {
    position: absolute;
    right: 27px;
    top: 270px;
    list-style: none;
    text-align: right;
    color: var(--card-light);
    font-size: 15.5px;
    line-height: 24px;
  }
</style>
</head>
<body>

<section class="card card-front" aria-label="Card front">
  <svg class="card-shapes" viewBox="0 0 595 333" preserveAspectRatio="none" aria-hidden="true">
    <path d="M333,0 Q470,74 595,87 L595,0 Z" fill="var(--card-light)"/>
    <path d="M380,21 Q480,54 595,57 L595,62 Q480,60 380,21 Z" fill="var(--card-dark)"/>
    <path d="M0,245 Q150,262 263,333 L0,333 Z" fill="var(--card-light)"/>
    <path d="M0,272 Q120,277 215,310 Q110,284 0,279 Z" fill="var(--card-dark)"/>
  </svg>
  <p class="brand-name">Harbor Ledger</p>
</section>

<section class="card card-back" aria-label="Card back">
  <svg class="card-shapes" viewBox="0 0 595 331" preserveAspectRatio="none" aria-hidden="true">
    <path d="M90,331 Q300,232 595,193 L595,331 Z" fill="var(--card-dark)"/>
    <path d="M205,290 Q400,242 595,231 L595,238 Q400,249 205,290 Z" fill="var(--card-light)"/>
  </svg>

  <p class="brand-name">Harbor Ledger</p>

  <div class="holder">
    <p class="name">Marcus Reed</p>
    <p class="role">Manager</p>
  </div>

  <ul class="contact-list">
    <li>Tel: 0011 987654321</li>
    <li>Mob: 0011 987654321</li>
    <li class="address">Addr: 42 Example Lane<br>P.O. Box 40112</li>
  </ul>

  <ul class="web-list">
    <li>info@harborledger-example.com.au</li>
    <li>www.harborledger-example.com.au</li>
  </ul>
</section>

</body>
</html>
```